tide-weavers - the complementary consultancy

Please create a powerpoint template for us. We are a management consultancy that combines the business aspects with the values and culture-oriented aspects (= we are a complementary consultancy).

Please also take into account the following key data:
- Logo see appendix
- Colors in the logo see appendix

I need a quick fix :))

----------------
We are a consulting company that offers its customers complementary advice for mission-critical transformation projects.

Complementary counseling integrates different perspectives and approaches to offer more comprehensive solutions and better understanding. By combining methods, models and theories from different disciplines, she supports individual needs and goals of clients or organizations.

The core idea is that connecting different approaches leads to a more comprehensive understanding and more effective solutions. It develops bespoke solutions tailored to specific needs and contexts, rather than being limited to a single theory or method.

Target Market(s)

Top management of QOR companies

Font styles to use
Other font styles liked:
• Roboto

Requirements
Must have
• PPT template including cover page, table of contents, content page, back page
Should not have
• no new logo

```html
<!DOCTYPE html>
<html lang="en">
<head>
<meta charset="utf-8">
<title>Tide Weavers – Presentation Template</title>
<link href="https://fonts.googleapis.com/css2?family=Roboto:wght@300;400;500;700;900&family=Montserrat:wght@700;800&display=swap" rel="stylesheet">
<style>
  :root{
    --board:#4a4b4d;
    --blue:#1c98dc;
    --blue-bright:#22a6e8;
    --ink:#1d1d1f;
    --muted:#555a60;
    --rule:#a9acb0;
    --band:#f3f2f0;
    --card-line:#9fd0ee;
    --white:#ffffff;
  }
  *{margin:0;padding:0;box-sizing:border-box}
  html,body{width:1200px;height:3914px;overflow:hidden;background:var(--board)}
  body{position:relative;font-family:"Roboto",Arial,sans-serif;color:var(--ink)}
  .slide{position:absolute;left:105px;width:1002px;height:563px;overflow:hidden;background:var(--white)}

  .brand{position:absolute;display:flex;align-items:center;gap:10px;font-family:"Roboto",Arial,sans-serif;font-weight:500;letter-spacing:2px;white-space:nowrap}
  .brand .dot{width:12px;height:12px;border-radius:50%;background:currentColor}
  .brand--blue{color:var(--blue)}
  .brand--white{color:var(--white)}

  .tab{position:absolute;background:var(--blue);color:var(--white);font-weight:700;display:flex;align-items:center;justify-content:center;font-family:"Montserrat",Arial,sans-serif}

  .band{position:absolute;left:0;top:0;width:100%;height:83px;background:var(--band)}

  /* Cover */
  .cover__photo{position:absolute;inset:0;background:linear-gradient(120deg,#2d333b 0%,#4a525b 45%,#30363d 75%,#23272c 100%)}
  .cover__bar{position:absolute;left:3px;top:428px;width:8px;height:85px;background:var(--blue)}
  .cover__title{position:absolute;left:47px;top:420px;font-weight:700;font-size:40px;line-height:49px;color:var(--white)}
  .cover__title span{display:block;color:var(--blue-bright)}

  /* Contents */
  .toc__row{position:absolute;left:38px;width:926px;height:73px;border-bottom:1.5px solid var(--rule)}
  .toc__title{position:absolute;left:0;top:0;font-family:"Montserrat",Arial,sans-serif;font-weight:700;font-size:15px;color:var(--blue)}
  .toc__sub{position:absolute;left:0;top:24px;font-size:12px;color:var(--ink)}
  .toc__num{position:absolute;right:4px;top:16px;font-size:12px;color:var(--ink)}

  /* About */
  .lead{position:absolute;font-size:19px;line-height:26px;color:var(--ink)}
  .body{position:absolute;font-size:13.4px;line-height:21px;color:var(--muted)}

  /* Services */
  .card{position:absolute;width:459px;height:196px;border:1.5px solid var(--card-line)}
  .card__icon{position:absolute;left:25px;top:33px;width:75px;height:75px;border-radius:50%;background:var(--blue);display:flex;align-items:center;justify-content:center}
  .card__title{position:absolute;left:125px;top:22px;font-size:18px}
  .card__text{position:absolute;left:125px;top:50px;width:310px;font-size:12.3px;line-height:16.7px;color:var(--muted)}

  /* Solutions */
  .sol__photo{position:absolute;left:0;top:83px;width:513px;height:480px;background:radial-gradient(circle at 48% 30%,#f3c27a 0%,#a86c3e 12%,#3b4452 38%,#1e2631 70%,#151a21 100%)}
  .sol__lead{position:absolute;left:574px;top:140px;width:368px;font-size:18.5px;line-height:22.5px}
  .sol__body{position:absolute;left:574px;top:258px;width:365px;font-size:11.8px;line-height:16.7px;color:var(--muted)}

  /* Back page */
  .back{background:var(--blue-bright)}
  .back__photo{position:absolute;inset:0;background:linear-gradient(180deg,rgba(20,120,190,.35) 0%,rgba(25,130,200,.55) 45%,rgba(34,166,232,0) 85%)}
  .back__rule{position:absolute;left:365px;width:305px;height:1.5px;background:rgba(255,255,255,.85)}
  .back__title{position:absolute;text-align:center;font-weight:300;font-size:62px;color:var(--white)}
  .contact{position:absolute;top:486px;display:flex;gap:12px;color:var(--white);font-size:15px;line-height:22px}
  .contact__icon{width:30px;height:30px;border-radius:50%;background:var(--white);display:flex;align-items:center;justify-content:center;margin-top:6px}
</style>
</head>
<body>

<!-- Cover -->
<section class="slide cover" style="top:106px">
  <div class="cover__photo" role="img" aria-label="Photo of two colleagues reviewing a document at an office desk"></div>
  <div class="brand brand--blue" style="left:47px;top:80px;font-size:19px"><span class="dot"></span>TIDE WEAVERS</div>
  <div class="cover__bar"></div>
  <h1 class="cover__title">WELCOME TO<span>TIDE WEAVERS</span></h1>
</section>

<!-- Table of contents -->
<section class="slide toc" style="top:720px">
  <div class="brand brand--blue" style="left:38px;top:40px;font-size:19px"><span class="dot"></span>TIDE WEAVERS</div>
  <div class="tab" style="left:287px;top:26px;width:216px;height:58px;font-size:21px">Table of Contents</div>

  <div class="toc__row" style="top:116px"><div class="toc__title">Lorem Ipsum is simply</div><div class="toc__sub">Lorem ipsum dolor sit amet consectetur adipisc</div><div class="toc__num">02</div></div>
  <div class="toc__row" style="top:188px"><div class="toc__title">Lorem Ipsum is simply</div><div class="toc__sub">Lorem ipsum dolor sit amet consectetur adipisc</div><div class="toc__num">03</div></div>
  <div class="toc__row" style="top:261px"><div class="toc__title">Lorem Ipsum is simply</div><div class="toc__sub">Lorem ipsum dolor sit amet consectetur adipisc</div><div class="toc__num">04</div></div>
  <div class="toc__row" style="top:335px"><div class="toc__title">Lorem Ipsum is simply</div><div class="toc__sub">Lorem ipsum dolor sit amet consectetur adipisc</div><div class="toc__num">05</div></div>
  <div class="toc__row" style="top:407px"><div class="toc__title">Lorem Ipsum is simply</div><div class="toc__sub">Lorem ipsum dolor sit amet consectetur adipisc</div><div class="toc__num">06</div></div>
  <div class="toc__row" style="top:480px"><div class="toc__title">Lorem Ipsum is simply</div><div class="toc__sub">Lorem ipsum dolor sit amet consectetur adipisc</div><div class="toc__num">07</div></div>
</section>

<!-- About us -->
<section class="slide about" style="top:1334px">
  <div class="band"></div>
  <div class="brand brand--blue" style="left:16px;top:32px;font-size:14px"><span class="dot"></span>TIDE WEAVERS</div>
  <div class="tab" style="left:222px;top:20px;width:115px;height:47px;font-size:17px">About Us</div>
  <p class="lead" style="left:53px;top:130px;width:480px">Lorem ipsum dolor sit amet, consectetur adipiscing elit sed do eiusmod tempor incididunt ut labore</p>
  <p class="body" style="left:53px;top:202px;width:485px">Sed ut perspiciatis unde omnis iste natus error sit voluptatem accusantium doloremque laudantium, totam rem aperiam, eaque ipsa quae ab illo inventore veritatis et quasi architecto beatae vitae dicta sunt explicabo. Nemo enim ipsam voluptatem quia voluptas sit aspernatur aut odit aut fugit, sed quia consequuntur magni dolores eos qui</p>
  <p class="body" style="left:53px;top:326px;width:485px">Sed ut perspiciatis unde omnis iste natus error sit voluptatem accusantium doloremque laudantium, totam rem aperiam, eaque ipsa quae ab illo inventore veritatis et quasi architecto beatae vitae dicta sunt explicabo. Nemo enim ipsam voluptatem quia voluptas sit aspernatur aut odit aut fugit, sed quia consequuntur magni dolores eos qui ratione voluptatem sequi nesciunt. Neque porro quisquam est, qui dolorem ipsum quia dolor sit amet, consectetur, adipisci velit, sed quia non numquam eius modi tempora incidunt ut labore et dolore magnam aliquam</p>
</section>

<!-- Services -->
<section class="slide services" style="top:1947px">
  <div class="band"></div>
  <div class="brand brand--blue" style="left:16px;top:32px;font-size:14px"><span class="dot"></span>TIDE WEAVERS</div>
  <div class="tab" style="left:222px;top:20px;width:102px;height:47px;font-size:17px">Services</div>

  <div class="card" style="left:32px;top:114px">
    <div class="card__icon"><svg width="38" height="34" viewBox="0 0 38 34" fill="none" stroke="#fff" stroke-width="2.4"><rect x="10" y="12" width="18" height="4"/><line x1="19" y1="16" x2="19" y2="30"/><rect x="2" y="8" width="6" height="12"/><rect x="30" y="8" width="6" height="12"/></svg></div>
    <div class="card__title">Lorem Ipsum</div>
    <p class="card__text">Sed ut perspiciatis unde omnis iste natus error sit voluptatem accusantium doloremque laudantium, totam rem aperiam, eaque ipsa quae ab illo inventore veritatis et quasi architecto beatae vitae dicta sunt explicabo. Nemo enim ipsam voluptatem quia voluptas sit aspernatur aut odit aut fugit, sed quia consequuntur magni dolores eos qui</p>
  </div>
  <div class="card" style="left:512px;top:114px">
    <div class="card__icon"><svg width="38" height="36" viewBox="0 0 38 36" fill="none" stroke="#fff" stroke-width="2.4"><rect x="14" y="4" width="20" height="16"/><polyline points="18,16 22,12 26,14 30,8"/><circle cx="8" cy="8" r="4"/><line x1="8" y1="13" x2="8" y2="32"/></svg></div>
    <div class="card__title">Lorem Ipsum</div>
    <p class="card__text">Sed ut perspiciatis unde omnis iste natus error sit voluptatem accusantium doloremque laudantium, totam rem aperiam, eaque ipsa quae ab illo inventore veritatis et quasi architecto beatae vitae dicta sunt explicabo. Nemo enim ipsam voluptatem quia voluptas sit aspernatur aut odit aut fugit, sed quia consequuntur magni dolores eos qui</p>
  </div>
  <div class="card" style="left:32px;top:328px">
    <div class="card__icon"><svg width="38" height="34" viewBox="0 0 38 34" fill="none" stroke="#fff" stroke-width="2.4"><rect x="6" y="2" width="26" height="14"/><line x1="11" y1="7" x2="27" y2="7"/><line x1="11" y1="11" x2="22" y2="11"/><circle cx="9" cy="23" r="3"/><circle cx="19" cy="23" r="3"/><circle cx="29" cy="23" r="3"/><line x1="3" y1="32" x2="35" y2="32"/></svg></div>
    <div class="card__title">Lorem Ipsum</div>
    <p class="card__text">Sed ut perspiciatis unde omnis iste natus error sit voluptatem accusantium doloremque laudantium, totam rem aperiam, eaque ipsa quae ab illo inventore veritatis et quasi architecto beatae vitae dicta sunt explicabo. Nemo enim ipsam voluptatem quia voluptas sit aspernatur aut odit aut fugit, sed quia consequuntur magni dolores eos qui</p>
  </div>
  <div class="card" style="left:512px;top:328px">
    <div class="card__icon"><svg width="36" height="34" viewBox="0 0 36 34" fill="none" stroke="#fff" stroke-width="2.4"><rect x="8" y="2" width="26" height="20"/><circle cx="13" cy="18" r="5"/><path d="M3 32c0-6 4-9 10-9s10 3 10 9"/></svg></div>
    <div class="card__title">Lorem Ipsum</div>
    <p class="card__text">Sed ut perspiciatis unde omnis iste natus error sit voluptatem accusantium doloremque laudantium, totam rem aperiam, eaque ipsa quae ab illo inventore veritatis et quasi architecto beatae vitae dicta sunt explicabo. Nemo enim ipsam voluptatem quia voluptas sit aspernatur aut odit aut fugit, sed quia consequuntur magni dolores eos qui</p>
  </div>
</section>

<!-- Solutions -->
<section class="slide solutions" style="top:2561px">
  <div class="band"></div>
  <div class="brand brand--blue" style="left:16px;top:32px;font-size:14px"><span class="dot"></span>TIDE WEAVERS</div>
  <div class="tab" style="left:222px;top:20px;width:110px;height:47px;font-size:17px">Solutions</div>
  <div class="sol__photo" role="img" aria-label="Photo of a hand holding a glowing light bulb against a dark background"></div>
  <p class="sol__lead">Et harum quidem rerum facilis est et expedita distinctio. Nam libero tempore, cum soluta nobis est eligendi optio cumque nihil impedit</p>
  <p class="sol__body">At vero eos et accusamus et iusto odio dignissimos ducimus qui blanditiis praesentium voluptatum deleniti atque corrupti quos dolores et quas molestias excepturi sint occaecati cupiditate non provident, similique sunt in culpa qui officia deserunt mollitia animi, id est laborum et dolorum fuga. Et harum quidem rerum facilis est et expedita distinctio. Nam libero tempore, cum soluta nobis est eligendi optio cumque nihil impedit quo minus id quod maxime placeat facere possimus, omnis voluptas assumenda est, omnis dolor repellendus. Temporibus autem quibusdam et aut officiis debitis aut rerum necessitatibus saepe eveniet ut et voluptates repudiandae sint et molestiae non recusandae. Itaque earum rerum hic tenetur a sapiente delectus, ut aut reiciendis voluptatibus</p>
</section>

<!-- Back page -->
<section class="slide back" style="top:3175px">
  <div class="back__photo" role="img" aria-label="Blue-tinted photo of a team meeting around a table"></div>
  <div class="brand brand--white" style="left:0;width:1002px;justify-content:center;top:110px;font-size:26px"><span class="dot"></span>TIDE WEAVERS</div>
  <div class="back__rule" style="top:325px"></div>
  <div class="back__title" style="left:0;width:1035px;top:328px">Thank You</div>
  <div class="back__rule" style="top:411px"></div>

  <div class="contact" style="left:313px">
    <div class="contact__icon"><svg width="16" height="16" viewBox="0 0 24 24" fill="none" stroke="#1c98dc" stroke-width="2"><path d="M5 3h4l2 5-3 2a12 12 0 0 0 6 6l2-3 5 2v4a2 2 0 0 1-2 2A17 17 0 0 1 3 5a2 2 0 0 1 2-2z"/></svg></div>
    <div>Call Us<br>+1 555 010 4477</div>
  </div>
  <div class="contact" style="left:571px">
    <div class="contact__icon"><svg width="16" height="16" viewBox="0 0 24 24" fill="none" stroke="#1c98dc" stroke-width="2"><rect x="3" y="6" width="18" height="12"/><polyline points="3,6 12,13 21,6"/></svg></div>
    <div>Email Us<br>info@TideWeavers.com</div>
  </div>
</section>

</body>
</html>
```